Update informational website

I need a new modern site design for my website.

Here is the site: http://q.zt/kmRp

Here is a theme I liked: http://q.zt/kmRb

I am looking for something with clean lines and an exciting designs and graphics, please use images from brellowtide.com and track the images used so I can buy them if I like the design.

I just need the homepage and one interior page designed.

Colors
Bright Green #6ed30d
Dark Text #222
Lighter Text #444

Number of Pages Required

2 page

Font styles to use
Sans Serif

Requirements
Must have
• Clean, good spacing, responsive design, high resolution design

```html
<!DOCTYPE html>
<html lang="en">
<head>
<meta charset="utf-8">
<title>Mesa Glow Tinting</title>
<link href="https://fonts.googleapis.com/css2?family=Open+Sans:wght@400;600;700;800&display=swap" rel="stylesheet">
<style>
:root{
  --green:#6ed30d;
  --green-dark:#5cb80a;
  --dark:#222;
  --text:#444;
  --white:#fff;
  --grey:#d9d9d9;
  --footer:#252525;
}
*{box-sizing:border-box;margin:0;padding:0}
html,body{width:1200px;height:3529px;overflow:hidden}
body{position:relative;font-family:"Open Sans",Arial,sans-serif;color:var(--text);background:var(--white)}
.abs{position:absolute}
svg{display:block}

/* hero */
.hero-photo{left:0;top:0;width:1200px;height:600px;background:linear-gradient(100deg,#3b3f44 0%,#5a5f63 40%,#8a8f93 70%,#4a4d50 100%)}
.hero-shade{left:0;top:0;width:1200px;height:600px;background:linear-gradient(90deg,rgba(0,0,0,.45),rgba(0,0,0,0) 60%)}
.topbar{left:165px;top:22px;width:870px;height:20px;font-size:11px;color:var(--white);display:flex;align-items:center;gap:22px}
.topbar .ico{display:inline-flex;align-items:center;gap:6px}
.social{margin-left:auto;display:flex;gap:18px}
.social span{width:11px;height:11px;border-radius:50%;background:var(--white);display:block}
.topline{left:165px;top:58px;width:870px;height:1px;background:rgba(255,255,255,.35)}
.brand{left:165px;top:84px;display:flex;align-items:center;gap:8px;color:var(--green);font-weight:700;font-size:17px;line-height:1.1;width:140px}
.brand i{width:14px;height:14px;background:var(--green);display:block;flex:none}
.nav{left:590px;top:60px;display:flex;gap:0;font-size:11px;color:var(--white)}
.nav a{color:inherit;text-decoration:none;padding:30px 16px 0;border-top:3px solid transparent}
.nav a.active{color:var(--green);border-top-color:var(--green)}
.hero-title{left:165px;top:196px;font-size:55px;line-height:68px;font-weight:600;color:var(--white);letter-spacing:-.5px}
.hero-title b{color:var(--green);font-weight:700;display:block}
.btn-contact{left:165px;top:438px;width:211px;height:54px;background:var(--white);border-left:12px solid var(--green);color:var(--green);font-weight:700;font-size:17px;display:flex;align-items:center;justify-content:center;letter-spacing:.5px}
.dots{left:960px;top:440px;display:flex;flex-direction:column;gap:16px}
.dots span{width:10px;height:10px;border-radius:50%;background:rgba(255,255,255,.7);display:block}
.dots span.on{background:var(--green)}

/* services */
.section-title{width:1200px;left:0;text-align:center;font-weight:700;letter-spacing:.3px}
.services-title{top:728px;font-size:35px;color:var(--white)}
.services-sub{top:788px;font-size:19px;color:var(--white);text-align:center;width:1200px;left:0}
.road-photo{left:0;top:915px;width:1200px;height:930px;background:linear-gradient(180deg,#cfd1d3 0%,#9a9ea2 35%,#e2e3e4 55%,#6d7175 80%,#b9bcbf 100%)}
.card-row{left:165px;top:892px;width:870px;height:266px;display:flex;background:var(--white);box-shadow:0 6px 20px rgba(0,0,0,.25)}
.card-arrow{width:52px;display:flex;align-items:center;justify-content:center;background:var(--white)}
.card{flex:1;position:relative;padding:48px 40px 0 42px;color:var(--white)}
.card-auto{background:linear-gradient(120deg,#2d3135,#55595d 60%,#3a3d40)}
.card-comm{background:var(--green)}
.card h3{font-size:35px;line-height:40px;font-weight:700;text-transform:uppercase}
.card p{font-size:15px;margin-top:2px}
.card .est{display:inline-block;margin-top:26px;font-size:12px;font-weight:700;padding:8px 14px;letter-spacing:.3px}
.card-auto .est{background:var(--green);color:var(--white)}
.card-comm .est{background:var(--dark);color:var(--white)}

/* about */
.about-card{left:165px;top:1247px;width:870px;height:588px;background:var(--white);box-shadow:0 6px 24px rgba(0,0,0,.2)}
.about-title{top:1356px;font-size:35px;color:var(--green)}
.about-text{left:253px;top:1440px;width:700px;font-size:14px;line-height:29px;color:var(--dark)}
.tabs{left:253px;top:1660px;width:700px;display:flex;justify-content:space-between;font-size:13px;font-weight:700;color:var(--green)}
.tabs span{padding-bottom:12px;display:flex;align-items:center;gap:8px}
.tabs span.on{border-bottom:2px solid var(--green)}

/* tint guide */
.guide-title{top:1894px;font-size:35px;color:var(--green)}
.car-photo{left:388px;top:2005px;width:412px;height:290px;border-radius:60px 60px 20px 20px;background:linear-gradient(180deg,#4d5155 0%,#a8acb0 40%,#7a7e82 75%,#2b2d2f 100%)}
.car-label{left:550px;top:2032px;width:90px;text-align:center;font-size:29px;color:var(--white);font-weight:600}
.round-arrow{width:44px;height:44px;border-radius:50%;background:var(--green);display:flex;align-items:center;justify-content:center}
.btn-estimate{left:494px;top:2343px;width:212px;height:43px;background:var(--green);color:var(--white);font-weight:700;font-size:16px;display:flex;align-items:center;justify-content:center;gap:6px}

/* inquire */
.inquire-title{top:2534px;font-size:37px;color:var(--white)}
.inquire-sub{left:0;top:2600px;width:1200px;text-align:center;font-size:20px;color:var(--white)}
.inquire-sub b{font-weight:700}
.play{left:562px;top:2656px;width:76px;height:76px;border-radius:50%;background:var(--white);display:flex;align-items:center;justify-content:center}
.field{height:48px;background:var(--white);font-size:14px;color:#b5b5b5;display:flex;align-items:center;padding:0 14px;justify-content:space-between}
.field em{font-style:normal;color:var(--green);font-weight:700;font-size:14px}
.btn-inquire{left:165px;top:2946px;width:870px;height:49px;background:var(--dark);color:var(--white);font-weight:700;font-size:15px;display:flex;align-items:center;justify-content:center;letter-spacing:.3px}

/* map */
.map{left:0;top:3030px;width:1200px;height:350px;background:linear-gradient(135deg,#e4e4e4,#cfcfcf 50%,#e9e9e9)}
.pin-card{left:453px;top:3236px;width:148px;height:48px;background:var(--white);font-size:10px;line-height:14px;color:var(--dark);padding:8px 10px;box-shadow:0 2px 6px rgba(0,0,0,.2)}
.map-icons{left:502px;top:3302px;display:flex;gap:8px}
.map-icons span{width:38px;height:38px;border:2px solid var(--white);background:var(--white);display:flex;align-items:center;justify-content:center;border-radius:4px}
.map-icons span.on{background:var(--green)}

/* footer */
.footer{left:0;top:3376px;width:1200px;height:153px;background:var(--footer)}
.footer-social{left:180px;top:3430px;display:flex;gap:0}
.footer-social span{width:44px;height:34px;border-right:1px solid #3a3a3a;display:flex;align-items:center;justify-content:center}
.footer-social span i{width:12px;height:12px;border-radius:50%;background:#5a5a5a;display:block}
.newsletter{left:676px;top:3423px;width:360px;height:36px;background:#333;border-radius:3px;font-size:11px;color:#888;display:flex;align-items:center;padding:0 6px 0 18px;justify-content:space-between}
.newsletter b{background:var(--green);color:var(--white);font-size:11px;padding:6px 14px;border-radius:3px}
.copyright{left:165px;top:3494px;font-size:10px;color:#777}
.footer-links{left:840px;top:3494px;display:flex;gap:16px;font-size:10px;color:#999}
</style>
</head>
<body>

<!-- HERO -->
<div class="abs hero-photo" role="img" aria-label="Technician applying window film to a car in a workshop"></div>
<div class="abs hero-shade"></div>

<div class="abs topbar">
  <span class="ico"><svg width="10" height="10" viewBox="0 0 24 24"><path fill="#fff" d="M6.6 10.8a15 15 0 0 0 6.6 6.6l2.2-2.2c.3-.3.7-.4 1-.2 1.1.4 2.3.6 3.6.6.6 0 1 .4 1 1V20c0 .6-.4 1-1 1A17 17 0 0 1 3 4c0-.6.4-1 1-1h3.5c.6 0 1 .4 1 1 0 1.3.2 2.5.6 3.6.1.3 0 .7-.2 1z"/></svg>555.014.2290</span>
  <span class="ico"><svg width="10" height="12" viewBox="0 0 24 30"><path fill="#fff" d="M12 0a10 10 0 0 0-10 10c0 7.5 10 20 10 20s10-12.5 10-20A10 10 0 0 0 12 0zm0 14a4 4 0 1 1 0-8 4 4 0 0 1 0 8z"/></svg>1420 W. Copperline Rd Suite 4, Tempe, AZ 85000</span>
  <div class="social"><span></span><span></span><span></span><span></span></div>
</div>
<div class="abs topline"></div>

<div class="abs brand"><i></i>Mesa Glow Window Tint</div>

<nav class="abs nav">
  <a class="active">Home</a><a>Window Film Services</a><a>Film</a><a>About</a><a>Gallery</a><a>Contact</a>
</nav>

<h1 class="abs hero-title">MESA GLOW TINTING IS<b>NOT JUST ANOTHER<br>TINT SHOP.</b></h1>
<div class="abs btn-contact">CONTACT US</div>
<div class="abs dots"><span></span><span></span><span class="on"></span><span></span></div>

<!-- green band -->
<svg class="abs" style="left:0;top:560px" width="1200" height="460" viewBox="0 0 1200 460">
  <polygon points="0,20 600,100 1200,0 1200,360 0,460" fill="var(--green)"/>
</svg>

<!-- SERVICES / ABOUT background photo -->
<div class="abs road-photo" role="img" aria-label="Sports cars on a grey road background"></div>
<svg class="abs" style="left:0;top:900px" width="1200" height="120" viewBox="0 0 1200 120">
  <polygon points="0,0 1200,0 1200,0 0,120" fill="var(--green)"/>
</svg>

<h2 class="abs section-title services-title">OUR SERVICES</h2>
<p class="abs services-sub">We offer Residential, Commercial and Automotive tinting services.</p>

<div class="abs card-row">
  <div class="card-arrow"><svg width="14" height="22" viewBox="0 0 14 22"><path d="M11 2 3 11l8 9" stroke="var(--green)" stroke-width="3" fill="none"/></svg></div>
  <div class="card card-auto" role="img" aria-label="Technician tinting a car window">
    <h3>Automotive<br>Film</h3>
    <p>Heat, infrared, and UV protection</p>
    <span class="est">GET ESTIMATE</span>
  </div>
  <div class="card card-comm">
    <h3>Commercial &amp;<br>Residential</h3>
    <p>Your Valley Commercial Film Experts!</p>
    <span class="est">GET ESTIMATE</span>
  </div>
  <div class="card-arrow"><svg width="14" height="22" viewBox="0 0 14 22"><path d="M3 2l8 9-8 9" stroke="var(--dark)" stroke-width="3" fill="none"/></svg></div>
</div>

<!-- ABOUT -->
<div class="abs about-card"></div>
<svg class="abs" style="left:0;top:1780px" width="1200" height="120" viewBox="0 0 1200 120">
  <polygon points="0,0 1035,55 1035,0 1200,0 1200,120 0,120" fill="var(--white)"/>
</svg>
<h2 class="abs section-title about-title">ABOUT US</h2>
<p class="abs about-text">We specialize in one thing and one thing only; Window Tinting. We offer Residential, Commercial and Automotive tinting services. Our philosophy is simple; do things right the first time! After 18 years we have learned that there is no such thing as a small job. Whether you need your personal car tinted, your new home protected or a complete face lift on your 10 story building, we believe that quality installation, attention to detail and customer service are the cornerstone's of a job well done.</p>
<div class="abs tabs">
  <span class="on"><svg width="14" height="14" viewBox="0 0 14 14"><circle cx="7" cy="7" r="6" fill="none" stroke="var(--green)" stroke-width="1.6"/><path d="M4 7l2 2 4-4" stroke="var(--green)" stroke-width="1.6" fill="none"/></svg>WE HAVE THE PRIVILEGE</span>
  <span>WE HAVE THE KNOWLEDGE</span>
  <span>WE HAVE THE TOOLS</span>
</div>

<!-- TINT GUIDE -->
<h2 class="abs section-title guide-title">TINT PERCENTAGE GUIDE</h2>
<div class="abs car-photo" role="img" aria-label="Front view of a silver sedan showing window tint level"></div>
<div class="abs car-label">80%</div>
<div class="abs round-arrow" style="left:225px;top:2126px"><svg width="12" height="16" viewBox="0 0 12 16"><path d="M9 2 3 8l6 6" stroke="#fff" stroke-width="2.5" fill="none"/></svg></div>
<div class="abs round-arrow" style="left:928px;top:2126px"><svg width="12" height="16" viewBox="0 0 12 16"><path d="M3 2l6 6-6 6" stroke="#fff" stroke-width="2.5" fill="none"/></svg></div>
<div class="abs btn-estimate">GET ESTIMATE <svg width="14" height="12" viewBox="0 0 14 12"><path d="M0 6h11M7 1l5 5-5 5" stroke="#fff" stroke-width="2.2" fill="none"/></svg></div>

<!-- INQUIRE -->
<svg class="abs" style="left:0;top:2430px" width="1200" height="700" viewBox="0 0 1200 700">
  <polygon points="0,0 1200,50 1200,645 0,660" fill="var(--green)"/>
</svg>
<h2 class="abs section-title inquire-title">INQUIRE NOW</h2>
<p class="abs inquire-sub">Watch the video and prepare to <b>be amaze.</b></p>
<div class="abs play"><svg width="24" height="28" viewBox="0 0 24 28"><polygon points="4,2 22,14 4,26" fill="var(--dark)"/></svg></div>

<div class="abs field" style="left:165px;top:2776px;width:268px">Name</div>
<div class="abs field" style="left:466px;top:2776px;width:268px">Email Address</div>
<div class="abs field" style="left:767px;top:2776px;width:268px">Contact Number</div>
<div class="abs field" style="left:165px;top:2859px;width:268px">Inquire tint for my <em>CAR ⌄</em></div>
<div class="abs field" style="left:466px;top:2859px;width:268px">Tint percentage <em>80% ⌄</em></div>
<div class="abs field" style="left:767px;top:2859px;width:268px">Tint percentage <em>80% ⌄</em></div>
<div class="abs btn-inquire">INQUIRE NOW</div>

<!-- MAP -->
<div class="abs map" role="img" aria-label="Street map showing the shop location"></div>
<svg class="abs" style="left:0;top:3025px" width="1200" height="80" viewBox="0 0 1200 80">
  <polygon points="0,0 1200,0 1200,50 0,70" fill="var(--green)"/>
</svg>
<svg class="abs" style="left:576px;top:3150px" width="24" height="32" viewBox="0 0 24 30"><path fill="#555" d="M12 0a10 10 0 0 0-10 10c0 7.5 10 20 10 20s10-12.5 10-20A10 10 0 0 0 12 0zm0 14a4 4 0 1 1 0-8 4 4 0 0 1 0 8z"/></svg>
<div class="abs pin-card">1420 W. Copperline Rd Suite 4,<br>Tempe, AZ 85000</div>
<div class="abs map-icons">
  <span class="on"><svg width="16" height="20" viewBox="0 0 24 30"><path fill="none" stroke="#fff" stroke-width="2.5" d="M12 2a8 8 0 0 0-8 8c0 6 8 17 8 17s8-11 8-17a8 8 0 0 0-8-8z"/><circle cx="12" cy="10" r="3" fill="#fff"/></svg></span>
  <span><svg width="20" height="14" viewBox="0 0 20 14"><rect x="1" y="1" width="18" height="12" fill="none" stroke="#333" stroke-width="1.6"/><path d="M1 1l9 7 9-7" fill="none" stroke="#333" stroke-width="1.6"/></svg></span>
  <span><svg width="16" height="16" viewBox="0 0 24 24"><path fill="none" stroke="#333" stroke-width="2" d="M6.6 10.8a15 15 0 0 0 6.6 6.6l2.2-2.2c.3-.3.7-.4 1-.2 1.1.4 2.3.6 3.6.6.6 0 1 .4 1 1V20c0 .6-.4 1-1 1A17 17 0 0 1 3 4c0-.6.4-1 1-1h3.5c.6 0 1 .4 1 1 0 1.3.2 2.5.6 3.6.1.3 0 .7-.2 1z"/></svg></span>
</div>

<!-- FOOTER -->
<footer class="abs footer"></footer>
<div class="abs footer-social"><span><i></i></span><span><i></i></span><span><i></i></span><span><i></i></span></div>
<div class="abs newsletter">Enter your email for our newsletter <b>Join</b></div>
<div class="abs copyright">© Copyright 2017 · hello@mesaglow.example</div>
<div class="abs footer-links"><span>About Us</span><span>Job</span><span>Terms of Service</span><span>Privacy</span><span>Policy</span></div>

</body>
</html>
```